Business Card Design

I need a business card design for a photography business that specializes in headshots and portraits.

Target Market(s)

Business professionals, actors, actresses

Industry/Entity Type

Business

Contact Information for Business Card

Cobalt Ridge Photography, Greg Whitlow, 5817 Kellerman Ave, Suite 416, Fort Wayne, IN 46915, 260.555.0187, www.cobaltridgephoto.example. greg.whitlow@cobaltridgephoto.example

Requirements
Must have
• The business card should state the type of photography services offered: headshots and portraits.

```html
<!DOCTYPE html>
<html lang="en">
<head>
<meta charset="utf-8">
<title>Cobalt Ridge Photography – Business Card</title>
<link rel="stylesheet" href="https://fonts.googleapis.com/css2?family=Gentium+Book+Plus&family=Arimo&display=swap">
<style>
  :root {
    --ink: #000000;
    --paper: #ffffff;
    --divider: #6b6b6b;
    --portrait-light: #f4f4f4;
    --portrait-shade: #cfcfcf;
  }
  * { margin: 0; padding: 0; box-sizing: border-box; }
  html, body {
    width: 1200px;
    height: 702px;
    overflow: hidden;
    background: var(--paper);
  }
  .card {
    position: absolute;
    left: 14px;
    top: 11px;
    width: 1175px;
    height: 682px;
    background: var(--ink);
  }
  .portrait-art {
    position: absolute;
    left: 80px;
    top: 83px;
    width: 438px;
    height: 560px;
    border-radius: 190px 190px 60px 60px;
    background: linear-gradient(160deg, var(--portrait-light), var(--portrait-shade));
  }
  .divider {
    position: absolute;
    left: 587px;
    top: 0;
    width: 1px;
    height: 682px;
    background: var(--divider);
  }
  .info-panel {
    position: absolute;
    left: 588px;
    top: 44px;
    width: 542px;
    height: 591px;
    background: var(--paper);
    color: var(--ink);
  }
  .info-panel p {
    position: absolute;
    line-height: 1;
    white-space: nowrap;
    text-align: right;
  }
  .studio-name, .photographer {
    font-family: "Gentium Book Plus", "Palatino Linotype", serif;
    font-size: 47px;
    right: 19px;
  }
  .studio-name { top: 31px; }
  .photographer { top: 175px; }
  .contact {
    font-family: "Arimo", Arial, sans-serif;
    font-size: 24.5px;
    right: 20px;
  }
  .street { top: 273px; }
  .city { top: 325px; }
  .services {
    top: 381px;
    font-style: italic;
  }
  .web { top: 438px; }
  .email { top: 491px; right: 14px; }
</style>
</head>
<body>
  <div class="card">
    <div class="portrait-art" role="img" aria-label="Silhouette illustration: a man's profile with a woman's profile cameo inside it"></div>
    <div class="divider"></div>
    <div class="info-panel">
      <p class="studio-name">Cobalt Ridge Photography</p>
      <p class="photographer">Greg Whitlow</p>
      <p class="contact street">5817 Kellerman Ave, Suite 416,</p>
      <p class="contact city">Fort Wayne, IN 46915, 260.555.0187,</p>
      <p class="contact services">Headshots &amp; Portraits</p>
      <p class="contact web">www.cobaltridgephoto.example</p>
      <p class="contact email">greg.whitlow@cobaltridgephoto.example</p>
    </div>
  </div>
</body>
</html>
```